Business Card Design for my Real Estate Investing Company

This is for a Real Estate Investing Company that will be serving the Las Vegas Valley. Id like the following slogan included: "Investing in Our Community" I have attached my logo. You will see the color tones I'm interested in..in my logo. I would like the card to be double-sided with a modern, professional look.
Target Market(s)
Homeowners, banks, real estate industry
Industry/Entity Type
Real Estate
Contact Information for Business Card
name: Dale Marwick
position: Managing Member
address: 4182 Corvello Pkwy ste 317-200
N. Las Vegas, NV 89117
phone: (702) 555-0143
fax: (702) 555-0187
email: SunridgeCrestPropertyGroup@mailbox-example.com
web: SunridgeCrestPropertyGroups.com
*At the bottom of the card I would like....
We buy houses for cash....no repairs, no commissions, no fees!
Logo Text
SUNRIDGE CREST PROPERTY GROUP "Investing in Our Community"
Font styles to use
Other font styles liked:
- Lora
Requirements
Must have
- On the back of the card, i'd like to have my logo large and the following statements:
- Are you considering selling your home? Want a simple, hassle-free transaction? We can help! We buy houses for cash and can close quickly! No need to do any repairs, no realtor commissions, no closing costs.....and no headaches. Let us help you with your real estate needs...!
Nice to have
- multiple colors 2 two tone on front and back

```html
<!DOCTYPE html>
<html lang="en">
<head>
<meta charset="utf-8">
<title>Sunridge Crest Property Group — Business Card</title>
<link href="https://fonts.googleapis.com/css2?family=Lora:ital,wght@0,400;0,600;0,700;1,400&display=swap" rel="stylesheet">
<style>
  :root {
    --page-bg: #e9e6e1;
    --card-white: #ffffff;
    --brand-blue: #1a7cc9;
    --brand-blue-deep: #0b5ca3;
    --brand-blue-light: #2b8fdb;
    --ink: #2c2c2c;
    --ink-soft: #555555;
    --on-blue: #ffffff;
    --on-blue-soft: rgba(255,255,255,.88);
  }
  * { margin: 0; padding: 0; box-sizing: border-box; }
  html, body {
    width: 1200px; height: 780px; overflow: hidden;
    background: var(--page-bg);
    font-family: "Lora", Georgia, serif;
  }
  .stage {
    width: 1200px; height: 780px;
    display: flex; align-items: center; justify-content: center; gap: 40px;
  }
  .card {
    position: relative;
    width: 560px; height: 320px;
    border-radius: 3px;
    box-shadow: 0 10px 28px rgba(0,0,0,.18), 0 1px 3px rgba(0,0,0,.12);
    overflow: hidden;
  }

  /* Front */
  .card--front { background: var(--card-white); }
  .front-brand {
    position: absolute; top: 32px; right: 36px;
    text-align: right;
  }
  .brand-mark {
    display: flex; align-items: center; justify-content: flex-end; gap: 10px;
  }
  .brand-square {
    width: 22px; height: 22px; background: var(--brand-blue); flex: none;
  }
  .brand-name {
    font-weight: 700; color: var(--brand-blue);
    font-size: 24px; letter-spacing: .5px; line-height: 1.1;
  }
  .slogan {
    margin-top: 6px;
    font-size: 11px; letter-spacing: 3px; color: var(--ink-soft);
  }
  .front-contact {
    position: absolute; left: 38px; bottom: 26px; right: 30px;
  }
  .accent-bar {
    position: absolute; left: 0; top: 146px;
    width: 22px; height: 30px; background: var(--brand-blue);
  }
  .person-name {
    font-size: 21px; font-weight: 600; color: var(--brand-blue); line-height: 1.1;
  }
  .person-role {
    font-size: 13px; color: var(--ink); margin-bottom: 10px;
  }
  .contact-line {
    font-size: 12px; color: var(--ink); line-height: 1.55;
  }
  .contact-label { color: var(--brand-blue); }
  .web-accent { color: var(--brand-blue); }
  .tagline {
    margin-top: 8px;
    font-size: 14px; color: var(--brand-blue);
  }

  /* Back */
  .card--back {
    background: radial-gradient(ellipse at 45% 35%, var(--brand-blue-light) 0%, var(--brand-blue) 45%, var(--brand-blue-deep) 100%);
    color: var(--on-blue);
    display: flex; flex-direction: column; align-items: center; justify-content: center;
    text-align: center;
    padding: 0 36px;
  }
  .card--back .brand-mark { justify-content: center; }
  .card--back .brand-square { background: var(--on-blue); width: 24px; height: 24px; }
  .card--back .brand-name { color: var(--on-blue); font-size: 27px; }
  .card--back .slogan { color: var(--on-blue); font-size: 11px; margin-top: 6px; }
  .back-web {
    margin-top: 12px; font-size: 13px; letter-spacing: .3px;
  }
  .back-pitch {
    margin-top: 12px;
    font-size: 11px; line-height: 1.5; color: var(--on-blue-soft);
    max-width: 470px;
  }
</style>
</head>
<body>
<main class="stage">
  <section class="card card--front" aria-label="Business card front">
    <div class="front-brand">
      <div class="brand-mark">
        <span class="brand-square"></span>
        <span class="brand-name">SUNRIDGE CREST<br>PROPERTY GROUP</span>
      </div>
      <p class="slogan">“Investing in Our Community”</p>
    </div>
    <span class="accent-bar"></span>
    <div class="front-contact">
      <p class="person-name">Dale Marwick</p>
      <p class="person-role">Managing Member</p>
      <p class="contact-line"><span class="contact-label">P:</span> (702) 555-0143 | <span class="contact-label">F:</span> (702) 555-0187</p>
      <p class="contact-line"><span class="contact-label">E:</span> SunridgeCrestPropertyGroup@mailbox-example.com</p>
      <p class="contact-line">www.<span class="web-accent">SunridgeCrest</span>PropertyGroups.com</p>
      <p class="contact-line">4182 Corvello Pkwy ste 317-200, N. Las Vegas, NV 89117</p>
      <p class="tagline">We buy houses for cash....no repairs, no commissions, no fees</p>
    </div>
  </section>

  <section class="card card--back" aria-label="Business card back">
    <div class="brand-mark">
      <span class="brand-square"></span>
      <span class="brand-name">SUNRIDGE CREST<br>PROPERTY GROUP</span>
    </div>
    <p class="slogan">“Investing in Our Community”</p>
    <p class="back-web">www.SunridgeCrestPropertyGroups.com</p>
    <p class="back-pitch">Are you considering selling your home? Want a simple, hassle-free transaction? We can help! We buy houses for cash and can close quickly! No need to do any repairs, no realtor commissions, no closing costs.....and no headaches. Let us help you with your real estate needs...!</p>
  </section>
</main>
</body>
</html>
```